Industry leading Property Management Company needs a flyer!

We need a brochure describing our fees and a basic description of what we do. This brochure will be printed, to be given to prospective clients, but we would also like an electronic version that can be downloaded from our website as a PDF. This project will be printed double sided, on standard 8.5" x 11" paper, in landscape mode, as a tri-fold brochure.

Target Market(s)

Real estate investors, but more importantly, first time investors. Many of our clients are "accidental landlords" who had their property for sale that didn't sell, so they are trying property management and rental investing for the first time. TRUST is their biggest fear

Font styles to use
Sans Serif

Requirements
Must have
• Must incorporate our logo, elements of our pricing list, and incorporate the text from our home page and "property management info" page (www.corvalinkrent.net). A word document specifying this text has been included in the project brief.
• Additionally, I am thinking this will be a simple, single piece of paper, in landscape mode, printed on both sides, in a Tri-fold. The front of the brochure will have the logo/name of the company, along with the Harbor Tenant Medals logos. I am thinking the first inside pane, when someone opens up the brochure, will have reference text #1 and #3. The 3 tiered pricing plan might occupy the 2nd and 3rd of the three panes on the inside fold. Reference text #4, 5, and 6 will occupy the next pane (see brief for handwritten layout). Then, the very back pane (when it is folded and shut) will have reference text #2 and our company contact information, plus any kind of stock photos, etc.
Nice to have
• Our main market will be first time investors, so we need to display and demonstrate relationships, and trust. We would prefer stock photos that incorporate families, children, or other images that solidify peace of mind.

```html
<!DOCTYPE html>
<html lang="en">
<head>
<meta charset="utf-8">
<title>Corvalink Rent Management – Pricing Brochure</title>
<link rel="stylesheet" href="https://fonts.googleapis.com/css2?family=Raleway:wght@300;400;500;600;700&display=swap">
<style>
  :root{
    --brand-blue:#0a5ccf;
    --bright-blue:#1d9ae0;
    --cell-blue:#a8d3ec;
    --header-dark:#333538;
    --ink:#2a2c30;
    --muted:#6b6f75;
    --rule:#8a8d92;
    --panel-grey:#f3f4f6;
    --cell-grey:#d9dadc;
    --white:#ffffff;
  }
  *{box-sizing:border-box;margin:0;padding:0}
  html,body{width:1200px;height:822px;overflow:hidden}
  body{font-family:"Raleway",sans-serif;color:var(--ink);background:#e6e7e9;position:relative}

  /* left panel */
  .panel-left{position:absolute;left:0;top:0;width:400px;height:822px;background:var(--panel-grey);overflow:hidden}
  .hero-photo{position:absolute;left:0;top:0;width:400px;height:152px;
    background:linear-gradient(100deg,#e9ecef 0%,#cfd6dc 35%,#8fa2ae 60%,#c7d3db 100%)}
  .about{position:absolute;left:0;top:152px;width:400px;height:228px;background:var(--brand-blue);color:var(--white);padding:34px 40px 0 44px}
  .about h2{font-size:20px;font-weight:700;margin-bottom:14px}
  .about p{font-size:14px;font-weight:300;line-height:1.4}
  .services{position:absolute;left:44px;top:396px;width:330px}
  .services h2{font-size:19px;font-weight:700;color:var(--brand-blue);margin-bottom:12px}
  .services .intro{font-size:14px;line-height:1.35;margin-bottom:18px}
  .service{display:flex;gap:16px;margin-bottom:10px}
  .service:last-child{margin-bottom:0}
  .service svg{flex:0 0 36px;width:36px;height:36px;stroke:var(--bright-blue);fill:none;stroke-width:1.6;stroke-linejoin:round;stroke-linecap:round}
  .service h3{font-size:12.5px;font-weight:700;margin-bottom:2px}
  .service p{font-size:10px;line-height:1.35;color:#3d4046}

  /* right panel */
  .panel-right{position:absolute;left:400px;top:0;width:800px;height:822px;background:var(--white)}
  .family-photo{position:absolute;left:0;top:660px;width:800px;height:162px;
    background:linear-gradient(90deg,#8a5a45 0%,#c99478 22%,#e8dccf 45%,#d7d9d6 62%,#a9805f 82%,#e7e2da 100%)}
  .sheet{position:absolute;left:0;top:0;width:800px;height:726px;background:var(--white);border-bottom-left-radius:64px}

  .pricing-title{position:absolute;left:40px;top:90px;font-size:20px;font-weight:700}
  .pricing-sub{position:absolute;left:40px;top:132px;font-size:14.5px;color:var(--muted);line-height:1.3}

  .plans{position:absolute;left:376px;top:22px;display:grid;grid-template-columns:repeat(3,128px)}
  .plan{display:flex;flex-direction:column;text-align:center}
  .plan-tab{height:24px;font-size:10px;font-weight:700;color:var(--white);display:flex;align-items:center;justify-content:center}
  .plan-tab.popular{background:var(--brand-blue);margin:0 6px}
  .plan-name{height:50px;background:var(--header-dark);color:var(--white);font-size:9.5px;font-weight:700;line-height:1.15;display:flex;flex-direction:column;justify-content:center;padding:0 6px}
  .plan-name span{font-weight:400;color:#bfc2c6}
  .plan-fee,.plan-coord,.plan-extra{background:var(--cell-blue);font-size:9.5px;line-height:1.1;display:flex;align-items:center;justify-content:center;border-bottom:1px solid var(--white);padding:0 6px;border-right:1px solid var(--white)}
  .plan-fee{height:30px}
  .plan-coord{height:24px}
  .plan-extra{height:28px}
  .plan-extra.empty{background:var(--cell-grey)}
  .plan-price{height:18px;background:var(--bright-blue);color:var(--white);font-size:9.5px;font-weight:700;display:flex;align-items:center;justify-content:center;border-right:1px solid var(--white)}

  .features{position:absolute;left:40px;top:200px;border-collapse:collapse;table-layout:fixed;width:720px}
  .features td{height:16.6px;border:1px solid var(--rule);font-size:9px;padding:0 4px;white-space:nowrap;overflow:hidden}
  .features td:first-child{width:336px}
  .features td.on{background:var(--cell-blue)}

  .footnotes{position:absolute;left:40px;top:608px;width:720px;font-size:7px;color:var(--muted);line-height:1.45}
  .footnotes p{margin-bottom:4px}
</style>
</head>
<body>

<section class="panel-left">
  <div class="hero-photo" role="img" aria-label="Property manager showing a bright apartment to a smiling couple"></div>
  <div class="about">
    <h2>About Us</h2>
    <p>Corvalink Rent Management has been serving the Winnipeg and surrounding areas since 1997. We offer world class management services to investors and tenants in the single family and multifamily rental market.</p>
  </div>
  <div class="services">
    <h2>Our Services</h2>
    <p class="intro">Corvalink Rent Management in Winnipeg offers some of the most premium services available for investors and tenants.</p>

    <div class="service">
      <svg viewBox="0 0 40 40"><path d="M4 20 20 6l16 14"/><path d="M9 16v18h22V16"/><path d="M17 34V24h6v10"/></svg>
      <div><h3>Property Management</h3><p>Using the latest technology and specially trained staff, we efficiently manage your property.</p></div>
    </div>
    <div class="service">
      <svg viewBox="0 0 40 40"><path d="M8 6h18v28H8z"/><path d="M12 13h10M12 18h10M12 23h6"/><circle cx="27" cy="26" r="6"/><path d="M31 30l5 5"/></svg>
      <div><h3>Leasing and Renewals</h3><p>We perform a comprehensive rental market evaluation to maximize your investment.</p></div>
    </div>
    <div class="service">
      <svg viewBox="0 0 40 40"><path d="M8 32 26 14"/><path d="M24 8a6 6 0 0 0 8 8l-4-4z"/><path d="M8 8l24 24"/><path d="M6 10l4-4"/></svg>
      <div><h3>Property Maintenance</h3><p>You'll never have to worry about that midnight call or have to scramble to find a plumber.</p></div>
    </div>
    <div class="service">
      <svg viewBox="0 0 40 40"><path d="M4 12h32v22H4z"/><path d="M4 24l10-8 8 6 14-10"/><path d="M10 34v-4M18 34v-6M26 34v-8"/></svg>
      <div><h3>Rehab and Construction</h3><p>We provide maintenance and repair services, and can also help you with larger construction projects.</p></div>
    </div>
    <div class="service">
      <svg viewBox="0 0 40 40"><path d="M6 10h24v24H6z"/><path d="M12 20l6 7 16-20"/></svg>
      <div><h3>Free Stuff</h3><p>At Corvalink we want to help smaller landlords. We believe in "giving back" which is why we volunteer hundreds of hours per year.</p></div>
    </div>
  </div>
</section>

<section class="panel-right">
  <div class="family-photo" role="img" aria-label="Family sharing a meal together in a bright kitchen"></div>
  <div class="sheet">
    <h2 class="pricing-title">Pricing</h2>
    <p class="pricing-sub">Complete transparency.<br>No locked in contracts *</p>

    <div class="plans">
      <div class="plan">
        <div class="plan-tab"></div>
        <div class="plan-name">"No More Midnight Phone Calls"<span>(Property Maintenance)</span></div>
        <div class="plan-fee">$54 monthly admin fee *</div>
        <div class="plan-coord">$25 Maintenance Coordination Fee</div>
        <div class="plan-extra empty"></div>
        <div class="plan-price">• $79 per month</div>
      </div>
      <div class="plan">
        <div class="plan-tab popular">MOST POPULAR</div>
        <div class="plan-name">"Full Service Management"<span>(Maintenance plus full Tenant Management)</span></div>
        <div class="plan-fee">$130 monthly management fee** *</div>
        <div class="plan-coord">$25 Maintenance Coordination Fee</div>
        <div class="plan-extra empty"></div>
        <div class="plan-price">• $155 per month</div>
      </div>
      <div class="plan">
        <div class="plan-tab"></div>
        <div class="plan-name">"Peace Of Mind"<span>(Full service plus court protection)</span></div>
        <div class="plan-fee">$130 monthly management fee** *</div>
        <div class="plan-coord">$25 Maintenance Coordination Fee</div>
        <div class="plan-extra">$20 Court protection package ***</div>
        <div class="plan-price">• $175 per month</div>
      </div>
    </div>

    <table class="features">
      <tr><td>24/7 emergency call centre and dispatch</td><td class="on"></td><td class="on"></td><td class="on"></td></tr>
      <tr><td>Tenant can create online maintenance tickets</td><td class="on"></td><td class="on"></td><td class="on"></td></tr>
      <tr><td>Automatic maintenance owner notifications</td><td class="on"></td><td class="on"></td><td class="on"></td></tr>
      <tr><td>Owner asked for permission before proceeding (except emergencies)</td><td class="on"></td><td class="on"></td><td class="on"></td></tr>
      <tr><td>Chat interface for all parties to communicate</td><td class="on"></td><td class="on"></td><td class="on"></td></tr>
      <tr><td>Customer service survey sent to every tenant after completion of job</td><td class="on"></td><td class="on"></td><td class="on"></td></tr>
      <tr><td>Actual contractor invoices uploaded into online owner portal</td><td class="on"></td><td class="on"></td><td class="on"></td></tr>
      <tr><td>Access to investor For Sale property listings (no commissions)</td><td class="on"></td><td class="on"></td><td class="on"></td></tr>
      <tr><td>Accounting and reporting</td><td class="on"></td><td class="on"></td><td class="on"></td></tr>
      <tr><td>Owner anonymity</td><td></td><td class="on"></td><td class="on"></td></tr>
      <tr><td>Portfolio management</td><td></td><td class="on"></td><td class="on"></td></tr>
      <tr><td>Tenant management</td><td></td><td class="on"></td><td class="on"></td></tr>
      <tr><td>Rent collection</td><td></td><td class="on"></td><td class="on"></td></tr>
      <tr><td>Warning letters, follow-up inspections, contractual disputes</td><td></td><td class="on"></td><td class="on"></td></tr>
      <tr><td>Meter readings</td><td></td><td class="on"></td><td class="on"></td></tr>
      <tr><td>Lease management</td><td></td><td class="on"></td><td class="on"></td></tr>
      <tr><td>Rent collection</td><td></td><td class="on"></td><td class="on"></td></tr>
      <tr><td>Warning letters, follow-up inspections, contractual disputes</td><td></td><td class="on"></td><td class="on"></td></tr>
      <tr><td>Meter readings</td><td></td><td class="on"></td><td class="on"></td></tr>
      <tr><td>Lease management</td><td></td><td class="on"></td><td class="on"></td></tr>
      <tr><td>Accounting and reporting</td><td></td><td class="on"></td><td class="on"></td></tr>
      <tr><td>Lease management</td><td></td><td class="on"></td><td class="on"></td></tr>
      <tr><td>Eligible for Group Insurance Plan (~45% discount off retail)</td><td></td><td class="on"></td><td class="on"></td></tr>
      <tr><td>Court protection ***</td><td></td><td></td><td class="on"></td></tr>
    </table>

    <div class="footnotes">
      <p>* management contracts have no term. If you find we are not a good fit for you, stop anytime.</p>
      <p>** Our fees are charged out at a flat rate. $130 is the maximum price for a single family home. Discounts are given for multiple units in the same building (ie $114 per unit for a duplex) and investors with multiple houses qualify for further discounts (eg. investor with 5 houses pay $110 per house per month). Management fees are NOT charged if the unit is vacant.</p>
      <p>*** Court protection includes all costs if it is necessary to take the tenant to court over unpaid rent or an eviction for noise complaints, etc. Typical court costs are approximately $650 or more.</p>
    </div>
  </div>
</section>

</body>
</html>
```